Buchcover-Design für psychologischen Ratgeber Morgens voller Mut!
Zielgruppe
Veröffentlichung psychologischer Ratgeber. Zielgruppe sind Erwachsene.
Aufgabenstellung
keine besondere Vorgaben, ein eyecatching-Cover wäre super. Der Titel des Buches lautet: Morgens voller Mut! Der Untertitel lautet: Heitere Seelenkunde für stille Kraft und Zuversicht
Autoren: Dr. Hanna Wiesmoor-Kalbach, Dr. Lukas Kalbach
Vielleicht macht es Sinn, einen Button mit: 199 Praxistipps auf dem Cover anzuführen.
Das Buch wird als Softcover und Ebook auf lesewelt veröffentlicht. Das Format ist 6 mal 9 Zoll und hat 425 Seiten.

```html
<!DOCTYPE html>
<html lang="de">
<head>
<meta charset="utf-8">
<title>Morgens voller Mut! – Buchcover</title>
<link href="https://fonts.googleapis.com/css2?family=Baloo+2:wght@800&family=Fira+Sans:wght@400;600;700;800&display=swap" rel="stylesheet">
<style>
  :root {
    --page-bg: #f1f1f1;
    --navy: #13294b;
    --sky-light: #fffbe6;
    --sky-warm: #ffe27a;
    --ground-yellow: #fff21a;
    --ground-amber: #ffc20a;
    --ground-orange: #ff9a10;
    --band-black: #0d0d0d;
    --white: #ffffff;
    --subtitle-light: #fdf3d2;
    --bird-tone: #26345a;
    --bird-beak: #f7c21c;
  }
  * { box-sizing: border-box; margin: 0; padding: 0; }
  html, body {
    width: 1152px; height: 1200px; overflow: hidden;
    background: var(--page-bg);
  }
  .cover {
    position: absolute; left: 209px; top: 50px;
    width: 734px; height: 1100px; overflow: hidden;
    background: linear-gradient(180deg, var(--ground-yellow) 0%, var(--ground-amber) 55%, var(--ground-orange) 100%);
    box-shadow: 0 20px 50px rgba(0,0,0,.18);
    font-family: "Fira Sans", sans-serif;
    color: var(--navy);
  }
  .cover__sky {
    position: absolute; left: 0; top: 0; width: 100%; height: 506px;
    background:
      radial-gradient(circle at 28% 38%, var(--sky-light) 0%, #fff6c8 30%, var(--sky-warm) 70%, #ffc64a 100%);
    clip-path: polygon(0 0, 100% 0, 100% 92%, 0 100%);
  }
  .cover__illustration {
    position: absolute; left: 260px; top: 130px; width: 330px; height: 490px;
    border-radius: 46% 46% 30% 30%;
    background: linear-gradient(160deg, var(--bird-beak) 0%, var(--bird-tone) 35%, var(--bird-tone) 100%);
    opacity: .92;
  }
  .publisher {
    position: absolute; left: 0; top: 400px; width: 180px; height: 88px;
    background: var(--band-black);
    display: flex; align-items: center; justify-content: center;
    color: var(--white); font-weight: 600; font-size: 19px;
  }
  .authors {
    position: absolute; left: 70px; right: 70px; top: 628px;
    font-weight: 800; font-size: 21px; letter-spacing: .2px;
    padding-bottom: 10px; border-bottom: 2px dashed var(--navy);
    white-space: nowrap;
  }
  .title {
    position: absolute; left: 40px; right: 30px; top: 668px;
    font-family: "Baloo 2", sans-serif; font-weight: 800;
    font-size: 122px; line-height: .9; letter-spacing: -1px;
  }
  .subtitle {
    position: absolute; left: 70px; right: 70px; top: 938px;
    border-top: 2px dashed var(--subtitle-light); padding-top: 14px;
  }
  .subtitle__kicker {
    display: block; color: var(--subtitle-light);
    font-weight: 600; font-size: 31px; letter-spacing: 7px;
  }
  .subtitle__line {
    display: block; font-weight: 800; font-size: 30px; margin-top: 4px;
  }
</style>
</head>
<body>
  <main class="cover">
    <div class="cover__sky"></div>
    <div class="cover__illustration" role="img" aria-label="Illustration: fröhlicher Tukan auf einem Ast"></div>
    <div class="publisher">Verlag Lichtblick</div>
    <p class="authors">Dr. Hanna Wiesmoor-Kalbach &amp; Dr. Lukas Kalbach</p>
    <h1 class="title">Morgens<br>voller Mut!</h1>
    <p class="subtitle">
      <span class="subtitle__kicker">HEITERE SEELENKUNDE</span>
      <span class="subtitle__line">für stille Kraft &amp; Zuversicht</span>
    </p>
  </main>
</body>
</html>
```